New word press website site design

We provide email marketing to aircraft brokers and dealers to assist in finding buyers for their aircraft.

Our target market to purchase our broadcasts are the aircraft sellers – NOT the buyers.

Our target market when sending the email broadcast, are the buyers (end users).

The website should target brokers and our email database targets the buyers.

We do not buy or sell aircraft as a company. We provide email marketing solutions to connect buyers and sellers of aircraft.

Our other site is planevista.net and will be redesigned soon. Please use it as a reference as far as general scope but they layout can be completely different and should include helicopters only as far as imagery. The colors should be similar as the logos are similar, however we do NOT want both sites to be identical in use of primary color

Plenty of images and sample broadcasts attached to use as needed throughout the site.

Headlines listed below with some text copy.

In the event that we need to add more text, please use standard greek text as a place holder for the purposes of the mockup design.

Need to have a “SUBSCRIBE” button to join our mailing list.

Possible Headlines:

Exclusively Showcasing Rotor Wing Aircraft to the Global Marketplace

Showcasing Pre-Owned Helicopters Available For Sale, Lease, Trade, or Wanted for Acquisition.

Mobile-optimized Email Campaigns that Render Correctly Across all Devices

Targeted worldwide recipients that currently own, operate, or have an interest in rotor wing aircraft

STRONGEST Rotor Wing Database in the Industry

Text/Copy:

HOME
Rotorcraft Parade is one of most powerful marketing tools in the industry to utilize in reaching targeted buyers of pre-owned helicopters. Rotorcraft Parade provides the rotor wing aircraft market with a fast, effective, and affordable email broadcast solution to utilize in the marketing of Helicopters for sale.

Developed Exclusively to Showcase Rotor Wing Aircraft to the Global marketplace, Rotorcraft Parade is a powerful tool designed to maximize leads and accelerate the sales process by providing the ability to reach a global network of Helicopter buyers in a matter of seconds.

DATABASE:

While Rotorcraft Parade is delivered to all known broker/dealers, our primary focus is in reaching end users. Our opt-in/opt-out recipient database is updated daily and developed specifically to deliver the latest details on helicopters available for sale or lease to the inboxes of a global network of Helicopter buyers and sellers.

· Helicopter Owners

· Helicopter Operators

· Helicopter Charter Services

· Helicopter Management Companies

· Corporate/Municipal Flight Departments

· Helicopter Pilots

· Senior Aviation Executives

· Wealth Management Firms

· High Net Worth Individuals

· Helicopter Broker/Dealers

Helicopter Tour/Travel Firms

· Off Shore Oil & Gas Production Firms

· Municipalities/Media/Medevac Firms

Our recipient database is continuously updated and developed specifically to reach buyers and sellers of Helicopters. This ensures that your Helicopter will be showcased to the right people. Rotorcraft Parade does not broadcast non-rotor wing aircraft and focuses exclusively on the Global Helicopter Market.

Broadcast Design:

Rotorcraft Parade broadcast ads are custom designed for you by incorporating your corporate image and branding. Because you have worked hard in developing your corporate image, we strive to maintain it while designing an ad that will showcase your Helicopter to its best advantage. Rotorcraft Parade utilizes Mobile-optimized Email Campaigns with Responsive Coding to render correctly across all devices

Once you have approved the design, we schedule the broadcast to be sent on the available date and time you request. The broadcast will link to your website and the results can be immediate. All email leads and replies will go to the email address that you provided.

Pricing:
Create a place holder for 3 Different Broadcast Packages

-Broadcast Package A
-Broadcast Package B
-Broadcast Package C

Target Market(s)

The target market is any person or company that has aircraft for sale. We work with brokers, dealers, and owners to assist in finding buyers for their aircraft using email marketing campaigns (Parade broadcasts).

Industry/Entity Type

Aviation

Colors
0255a3
00a990

Requirements
Nice to have
• Samples of helicopter for sale broadcast ads in /image gallery/slider

```html
<!DOCTYPE html>
<html lang="en">
<head>
<meta charset="utf-8">
<title>Rotorcraft Parade</title>
<link href="https://fonts.googleapis.com/css2?family=Roboto:wght@400;500;700&display=swap" rel="stylesheet">
<style>
:root{
  --navy:#0e2a49;
  --navy-deep:#0a2039;
  --navy-band:#0d2744;
  --green:#7cc242;
  --green-dark:#6aae33;
  --red:#e3151d;
  --paper:#efeeec;
  --ink:#1b1b1b;
  --muted:#555;
  --white:#fff;
}
*{box-sizing:border-box;margin:0;padding:0}
html,body{width:1200px;height:2995px;overflow:hidden}
body{font-family:'Roboto',sans-serif;background:var(--paper);color:var(--ink);position:relative}
a{color:inherit;text-decoration:none}

/* header */
.site-header{position:absolute;top:0;left:0;width:1200px;height:80px;background:var(--white)}
.brand{position:absolute;left:222px;top:26px;height:26px;display:flex;align-items:center;gap:8px;font-size:19px;font-weight:700;color:var(--navy);white-space:nowrap}
.brand-dot{width:12px;height:12px;border-radius:50%;background:var(--green)}
.main-nav{position:absolute;left:448px;top:32px;display:flex;gap:18px;font-size:12px;color:#333;white-space:nowrap}
.main-nav .active{color:var(--green-dark);border-bottom:2px solid var(--green);padding-bottom:6px}
.header-phone{position:absolute;left:798px;top:32px;font-size:12px;font-weight:700;color:#222;display:flex;align-items:center;gap:5px;white-space:nowrap}
.btn-subscribe{position:absolute;left:900px;top:26px;width:80px;height:27px;background:var(--green);color:#fff;font-size:10px;font-weight:700;display:flex;align-items:center;justify-content:center;letter-spacing:.3px}

/* hero */
.hero{position:absolute;top:80px;left:0;width:1200px;height:454px;background:linear-gradient(180deg,#8a8f95 0%,#c7a06a 55%,#3a3a2e 72%,#2a2b20 100%)}
.hero-title{position:absolute;top:190px;width:100%;text-align:center;color:#fff;font-size:26px;font-weight:700;line-height:32px}
.hero-dots{position:absolute;top:430px;left:550px;display:flex;gap:6px}
.hero-dots span{width:16px;height:3px;background:#fff}
.hero-dots span:first-child{background:var(--green)}

/* services */
.section-title{font-size:24px;font-weight:700;color:var(--ink);text-align:center}
.services{position:absolute;top:534px;left:0;width:1200px;height:622px;background:linear-gradient(90deg,var(--paper) 70%,#e4e3e1 100%)}
.services .section-title{margin-top:48px}
.lead{width:570px;margin:14px auto 0;text-align:center;font-size:11px;line-height:17px;color:var(--muted)}
.audience{position:absolute;top:166px;left:220px;width:760px;height:334px;display:flex}
.audience-photo{width:500px;height:334px;background:linear-gradient(160deg,#2f4d7a 0%,#8aa6cc 45%,#d9e2ee 100%)}
.audience-list{flex:1;background:var(--green);list-style:none;padding:22px 0 0 18px}
.audience-list li{font-size:11px;color:#fff;height:22.7px;display:flex;align-items:center;gap:7px;white-space:nowrap}
.services .note{position:absolute;top:522px;left:290px;width:620px}

/* welcome */
.welcome-band{position:absolute;top:1156px;left:0;width:1200px;height:314px;background:var(--navy-band)}
.welcome-band .section-title{color:#fff;margin-top:48px}
.video-frame{position:absolute;top:1262px;left:222px;width:758px;height:328px;border:6px solid #fff;background:radial-gradient(ellipse at 50% 55%,#4b4d52 0%,#111 60%);box-shadow:0 4px 10px rgba(0,0,0,.25)}
.play-icon{position:absolute;left:348px;top:130px}
.intro-cols{position:absolute;top:1620px;left:220px;width:760px;display:flex;justify-content:space-between}
.intro-cols p{width:336px;font-size:11px;line-height:17px;color:#333}
.intro-cols .divider{width:1px;background:#d6d5d2;height:78px}
.soft-rule{position:absolute;top:1770px;left:330px;width:540px;height:1px;background:linear-gradient(90deg,transparent,#cfcecb,transparent)}

/* pricing */
.pricing-head{position:absolute;top:1832px;width:1200px;text-align:center}
.pricing-head .section-title{font-size:25px}
.pricing-head p{font-size:11px;color:var(--muted);margin-top:6px}
.plan{position:absolute;top:1944px;width:254px;height:396px;background:#fff;text-align:center}
.plan-a{left:220px}
.plan-b{left:474px;top:1924px;width:252px;height:436px;box-shadow:0 4px 14px rgba(0,0,0,.15);z-index:2}
.plan-c{left:726px}
.plan-name{height:66px;background:var(--navy);color:#fff;font-size:18px;display:flex;align-items:center;justify-content:center;gap:5px}
.plan-b .plan-name{height:86px;background:var(--green);padding-top:20px}
.plan-price{height:70px;background:var(--navy-deep);color:#fff;font-size:22px;font-weight:700;display:flex;align-items:center;justify-content:center}
.plan-features{list-style:none;padding-top:22px}
.plan-features li{font-size:11px;color:#666;height:30.5px;display:flex;align-items:center;justify-content:center;border-bottom:1px solid #f0f0f0;margin:0 26px}
.plan-btn{display:flex;align-items:center;justify-content:center;width:200px;height:36px;margin:20px auto 0;background:var(--navy);color:#fff;font-size:11px;font-weight:700}
.plan-b .plan-btn{background:var(--green)}
.badge-popular{position:absolute;top:1912px;left:552px;width:96px;height:24px;background:var(--red);color:#fff;font-size:9px;font-weight:700;border-radius:12px;display:flex;align-items:center;justify-content:center;z-index:3}

/* broadcast design */
.design-band{position:absolute;top:2458px;left:0;width:1200px;height:278px;background:var(--green)}
.sample{position:absolute;border:4px solid #fff;box-shadow:0 3px 10px rgba(0,0,0,.3)}
.sample-one{top:2424px;left:220px;width:236px;height:306px;background:linear-gradient(180deg,#0c0c0c 0%,#b8121a 20%,#333 45%,#7a8794 70%,#111 100%)}
.sample-two{top:2500px;left:412px;width:200px;height:230px;background:linear-gradient(180deg,#0a0a0a 0%,#2b2b2b 40%,#8c8c8c 65%,#0a0a0a 100%);z-index:2}
.design-copy{position:absolute;top:2498px;left:674px;width:290px;color:#fff}
.design-copy h2{font-size:25px;font-weight:700}
.design-copy p{font-size:11px;line-height:17px;margin-top:14px}
.btn-proof{display:inline-flex;align-items:center;height:30px;padding:0 12px;margin-top:14px;background:var(--navy);color:#fff;font-size:11px;font-weight:700}

/* footer */
.site-footer{position:absolute;top:2736px;left:0;width:1200px;height:259px;background:var(--navy);color:#c9d2dd}
.footer-col{position:absolute;top:54px;font-size:11px;line-height:17px}
.footer-col h3{font-size:11px;font-weight:700;color:#fff;margin-bottom:10px;white-space:nowrap}
.footer-col ul{list-style:none}
.col-contact{left:220px}
.col-quick{left:428px}
.col-help{left:590px}
.col-news{left:740px}
.signup{display:flex;width:242px;height:34px;margin-top:4px}
.signup span{flex:1;background:#fff;color:#999;font-size:11px;display:flex;align-items:center;padding-left:10px}
.signup b{width:80px;background:var(--green);color:#fff;font-size:11px;display:flex;align-items:center;justify-content:center}
.social{display:flex;gap:8px;margin-top:16px}
.social span{width:24px;height:24px;border:1px solid #7d8ea3;background:#2a4565}
.copyright{position:absolute;top:196px;left:0;width:1200px;border-top:1px solid #23405f;padding-top:20px;text-align:center;font-size:11px;color:#9fb0c3}
</style>
</head>
<body>

<header class="site-header">
  <div class="brand"><span class="brand-dot"></span>Rotorcraft Parade</div>
  <nav class="main-nav">
    <a class="active">Home</a><a>Services</a><a>Broadcast Design</a><a>Pricing</a><a>Contact</a>
  </nav>
  <div class="header-phone">
    <svg width="11" height="11" viewBox="0 0 24 24"><path fill="#222" d="M6.6 10.8a15 15 0 0 0 6.6 6.6l2.2-2.2a1 1 0 0 1 1-.25 11.4 11.4 0 0 0 3.6.57 1 1 0 0 1 1 1V20a1 1 0 0 1-1 1A17 17 0 0 1 3 4a1 1 0 0 1 1-1h3.5a1 1 0 0 1 1 1c0 1.25.2 2.45.57 3.57a1 1 0 0 1-.25 1z"/></svg>
    1800 555 012
  </div>
  <a class="btn-subscribe">SUBSCRIBE</a>
</header>

<section class="hero" role="img" aria-label="Helicopter parked on a grass airfield at sunset">
  <h1 class="hero-title">Exclusively Showcasing Rotor Wing Aircraft<br>to the Global Marketplace</h1>
  <div class="hero-dots"><span></span><span></span><span></span><span></span><span></span></div>
</section>

<section class="services">
  <h2 class="section-title">What Services We offer</h2>
  <p class="lead">Rotorcraft Parade is one of most powerful marketing tools in the industry to utilize in reaching targeted buyers of pre-owned helicopters. Rotorcraft Parade provides the rotor wing aircraft market with a fast, effective, and affordable email broadcast solution to utilize in the marketing of Helicopters for sale.</p>
  <div class="audience">
    <div class="audience-photo" role="img" aria-label="Two helicopters flying over snowy mountains"></div>
    <ul class="audience-list">
      <li><svg width="9" height="9" viewBox="0 0 10 10"><path d="M1 5l3 3 5-7" stroke="#fff" stroke-width="1.8" fill="none"/></svg>Helicopter Owners</li>
      <li><svg width="9" height="9" viewBox="0 0 10 10"><path d="M1 5l3 3 5-7" stroke="#fff" stroke-width="1.8" fill="none"/></svg>Helicopter Operators</li>
      <li><svg width="9" height="9" viewBox="0 0 10 10"><path d="M1 5l3 3 5-7" stroke="#fff" stroke-width="1.8" fill="none"/></svg>Helicopter Charter Services</li>
      <li><svg width="9" height="9" viewBox="0 0 10 10"><path d="M1 5l3 3 5-7" stroke="#fff" stroke-width="1.8" fill="none"/></svg>Helicopter Management Companies</li>
      <li><svg width="9" height="9" viewBox="0 0 10 10"><path d="M1 5l3 3 5-7" stroke="#fff" stroke-width="1.8" fill="none"/></svg>Corporate/Municipal Flight Departments</li>
      <li><svg width="9" height="9" viewBox="0 0 10 10"><path d="M1 5l3 3 5-7" stroke="#fff" stroke-width="1.8" fill="none"/></svg>Helicopter Pilots</li>
      <li><svg width="9" height="9" viewBox="0 0 10 10"><path d="M1 5l3 3 5-7" stroke="#fff" stroke-width="1.8" fill="none"/></svg>Senior Aviation Executives</li>
      <li><svg width="9" height="9" viewBox="0 0 10 10"><path d="M1 5l3 3 5-7" stroke="#fff" stroke-width="1.8" fill="none"/></svg>Wealth Management Firms</li>
      <li><svg width="9" height="9" viewBox="0 0 10 10"><path d="M1 5l3 3 5-7" stroke="#fff" stroke-width="1.8" fill="none"/></svg>High Net Worth Individuals</li>
      <li><svg width="9" height="9" viewBox="0 0 10 10"><path d="M1 5l3 3 5-7" stroke="#fff" stroke-width="1.8" fill="none"/></svg>Helicopter Broker/Dealers</li>
      <li><svg width="9" height="9" viewBox="0 0 10 10"><path d="M1 5l3 3 5-7" stroke="#fff" stroke-width="1.8" fill="none"/></svg>Helicopter Tour/Travel Firms</li>
      <li><svg width="9" height="9" viewBox="0 0 10 10"><path d="M1 5l3 3 5-7" stroke="#fff" stroke-width="1.8" fill="none"/></svg>Off Shore Oil &amp; Gas Production Firms</li>
      <li><svg width="9" height="9" viewBox="0 0 10 10"><path d="M1 5l3 3 5-7" stroke="#fff" stroke-width="1.8" fill="none"/></svg>Municipalities/Media/Medevac Firms</li>
    </ul>
  </div>
  <p class="lead note">Our recipient database is continuously updated and developed specifically to reach buyers and sellers of Helicopters. This ensures that your Helicopter will be showcased to the right people. Rotorcraft Parade does not broadcast non-rotor wing aircraft and focuses exclusively on the Global Helicopter Market.</p>
</section>

<section class="welcome-band">
  <h2 class="section-title">Welcome Rotorcraft Parade</h2>
</section>
<div class="video-frame" role="img" aria-label="Video still of a silver helicopter in a dark studio">
  <svg class="play-icon" width="50" height="50" viewBox="0 0 50 50"><circle cx="25" cy="25" r="22" fill="none" stroke="#fff" stroke-width="3"/><path d="M20 15l14 10-14 10z" fill="#fff"/></svg>
</div>
<div class="intro-cols">
  <p>Rotorcraft Parade is one of most powerful marketing tools in the industry to utilize in reaching targeted buyers of pre-owned helicopters. Rotorcraft Parade provides the rotor wing aircraft market with a fast, effective, and affordable email broadcast solution to utilize in the marketing of Helicopters for sale.</p>
  <span class="divider"></span>
  <p>Developed Exclusively to Showcase Rotor Wing Aircraft to the Global marketplace, Rotorcraft Parade is a powerful tool designed to maximize leads and accelerate the sales process by providing the ability to reach a global network of Helicopter buyers in a matter of seconds.</p>
</div>
<div class="soft-rule"></div>

<div class="pricing-head">
  <h2 class="section-title">3 Different Broadcast Packages</h2>
  <p>Our Broadcast Packages Pricing below listed:</p>
</div>
<div class="badge-popular">MOST POPULAR</div>
<article class="plan plan-a">
  <div class="plan-name">Broadcast <b>Package A</b></div>
  <div class="plan-price">$39.99</div>
  <ul class="plan-features"><li>01. Awesome lorem ipsum dolor sit</li><li>02. Awesome lorem ipsum dolor sit</li><li>03. Awesome lorem ipsum dolor sit</li><li>04. Awesome lorem ipsum dolor sit</li><li>05. Awesome lorem ipsum dolor sit</li><li>06. Awesome lorem ipsum dolor sit</li></ul>
  <a class="plan-btn">SELECT PACKAGE</a>
</article>
<article class="plan plan-b">
  <div class="plan-name">Broadcast <b>Package B</b></div>
  <div class="plan-price">$59.99</div>
  <ul class="plan-features"><li>01. Awesome lorem ipsum dolor sit</li><li>02. Awesome lorem ipsum dolor sit</li><li>03. Awesome lorem ipsum dolor sit</li><li>04. Awesome lorem ipsum dolor sit</li><li>05. Awesome lorem ipsum dolor sit</li><li>06. Awesome lorem ipsum dolor sit</li></ul>
  <a class="plan-btn">SELECT PACKAGE</a>
</article>
<article class="plan plan-c">
  <div class="plan-name">Broadcast <b>Package C</b></div>
  <div class="plan-price">$29.99</div>
  <ul class="plan-features"><li>01. Awesome lorem ipsum dolor sit</li><li>02. Awesome lorem ipsum dolor sit</li><li>03. Awesome lorem ipsum dolor sit</li><li>04. Awesome lorem ipsum dolor sit</li><li>05. Awesome lorem ipsum dolor sit</li><li>06. Awesome lorem ipsum dolor sit</li></ul>
  <a class="plan-btn">SELECT PACKAGE</a>
</article>

<section class="design-band"></section>
<div class="sample sample-one" role="img" aria-label="Sample broadcast ad for a helicopter for sale"></div>
<div class="sample sample-two" role="img" aria-label="Sample broadcast ad for a wanted helicopter"></div>
<div class="design-copy">
  <h2>Broadcast Design</h2>
  <p>Rotorcraft Parade is one of most powerful marketing tools in the industry to utilize in reaching targeted buyers of pre-owned helicopters. Rotorcraft Parade provides the rotor wing aircraft market with a fast, effective, and affordable email broadcast solution to utilize in the marketing of Helicopters for sale.</p>
  <a class="btn-proof">RECEIVE A DESIGN PROOF</a>
</div>

<footer class="site-footer">
  <div class="footer-col col-contact">
    <h3>CONTACT INFO</h3>
    <p>226, lorem ipsum dolor,<br>doxis amet - 45895</p>
    <p style="margin-top:14px">T: 1800 555 012<br>E: info@rotorcraftparade.com</p>
  </div>
  <div class="footer-col col-quick">
    <h3>QUICK LINKS</h3>
    <ul><li>Home</li><li>Services</li><li>Broadcast Design</li><li>Pricing</li><li>Contact</li></ul>
  </div>
  <div class="footer-col col-help">
    <h3>HELPFUL LINKS</h3>
    <ul><li>Terms of Use</li><li>Privacy Policy</li><li>Sitemap</li><li>Contact Us</li></ul>
  </div>
  <div class="footer-col col-news">
    <h3>SUBSCRIBE TO JOIN OUR MAILING LIST</h3>
    <div class="signup"><span>Email Address</span><b>SUBSCRIBE</b></div>
    <div class="social"><span></span><span></span><span></span><span></span></div>
  </div>
  <p class="copyright">Copyright © 2018 Rotorcraft Parade. All Rights Reserved</p>
</footer>

</body>
</html>
```